Pilates trainer needs new website

Summary: I need a new, meaningful website in a 1-page format, but one that can be expanded if necessary. I teach in various studios and in the future also in companies. Therefore, the website should convey growth, joy, uniqueness, workout and a bit of luxury.
The website should be inviting.
Layout:
Introduction what I offer
A bit about me
Option to upload price list and timetable in PDF format
Studio address where I teach
The color scheme should be petrol, gold, and colors that match. Not too dark, please.
My current website www.movewell-brennach.de, new domain is corebalance-studio.com (I have already purchased it)
Logo file attached
I have attached a few suggestions but I am also happy to be surprised.

Target Market(s)

Pilates private and small groups,

Industry/Entity Type

Pilates teacher freelancer

Coding

Coded - Design and coding required

Number of Pages Required

1 page

Requirements
Must have
• Welcoming appearance, about me, pictures, offers, colors from the logo but don't get do dark, more fresh and a bit luxurious
Should not have
• Not too wild and going crazy with colors

```html
<!DOCTYPE html>
<html lang="en">
<head>
<meta charset="utf-8">
<title>Lena Hartwig – Pilates Studio Trainer</title>
<link rel="stylesheet" href="https://fonts.googleapis.com/css2?family=Cinzel:wght@400;500&family=Playfair+Display:ital,wght@1,400&family=Jost:wght@400;500;600&display=swap">
<style>
:root{
  --teal:#1aa597;
  --teal-dark:#128277;
  --gold:#c9a45e;
  --gold-light:#e6d3a8;
  --sand:#f1e9dc;
  --sand-deep:#e7dac4;
  --ink:#2e2e2e;
  --text:#555049;
  --white:#ffffff;
  --footer:#2f2f31;
  --footer-line:#4a4a4d;
}
*{box-sizing:border-box;margin:0;padding:0}
html,body{width:1200px;height:4820px;overflow:hidden}
body{position:relative;background:var(--white);font-family:"Jost",sans-serif;color:var(--text);font-size:15px;line-height:1.65}
.abs{position:absolute}
.script{font-family:"Playfair Display",serif;font-style:italic;color:var(--gold)}
.heading{font-family:"Cinzel",serif;color:var(--ink);font-weight:400;letter-spacing:2px;text-transform:uppercase;line-height:1.15}
.btn{position:absolute;display:inline-block;background:var(--teal);color:var(--white);font-weight:500;font-size:14px;letter-spacing:1px;text-transform:uppercase;padding:16px 28px;text-decoration:none}
.photo{position:absolute}

/* nav */
.nav{position:absolute;top:0;left:0;width:1200px;height:130px;z-index:3}
.nav a{position:absolute;top:56px;font-size:17px;color:var(--ink);text-decoration:none}
.nav a.active{color:var(--teal)}
.nav .contact{top:44px;background:var(--teal);color:var(--white);padding:10px 16px;font-weight:600;font-size:15px;letter-spacing:.5px}
.brand{position:absolute;left:520px;top:14px;width:160px;height:110px;display:flex;flex-direction:column;align-items:center;justify-content:center;gap:6px}
.brand .dot{width:14px;height:14px;border-radius:50%;background:var(--gold)}
.brand span{font-family:"Jost",sans-serif;font-weight:600;font-size:17px;color:var(--teal);letter-spacing:1px;text-align:center;line-height:1.2}

/* hero */
.hero-tag{left:112px;top:300px;font-size:32px;line-height:1.25;width:460px}
.hero-title{left:112px;top:400px;font-size:42px;width:460px}
.hero-btn{left:112px;top:580px}

.intro-label{left:0;width:1200px;text-align:center;top:905px;font-size:30px}
.intro-title{left:0;width:1200px;text-align:center;top:960px;font-size:44px}
.intro-text{left:230px;width:740px;top:1050px;text-align:center;font-size:15px}
.intro-text p{margin-bottom:18px}

.offer-label{left:0;width:1200px;text-align:center;top:1390px;font-size:72px;color:var(--gold-light);opacity:.8}

.offer-title{font-size:48px;letter-spacing:3px}
.offer-text{font-size:15px}
.offer-text p{margin-bottom:18px}

/* about */
.about-card{left:112px;top:3080px;width:988px;height:590px;background:var(--white);box-shadow:0 10px 40px rgba(0,0,0,.08)}
.about-label{left:40px;top:40px;font-size:30px}
.about-name{left:40px;top:90px;font-size:38px}
.about-text{left:40px;top:160px;width:540px;font-size:14.5px}
.about-text p{margin-bottom:16px}

/* testimonials */
.test-label{left:0;width:1200px;text-align:center;top:3830px;font-size:30px}
.test-title{left:0;width:1200px;text-align:center;top:3880px;font-size:44px}
.quote{position:absolute;top:3980px;width:480px;font-size:14.5px}
.quote b{display:block;margin-top:18px;font-weight:600;color:var(--ink)}
.dots{left:560px;top:4178px;display:flex;gap:10px}
.dots i{display:block;width:18px;height:4px;background:var(--sand-deep)}
.dots i.on{background:var(--gold)}

/* footer */
.footer{position:absolute;left:0;top:4240px;width:1200px;height:580px}
.f-brand{left:110px;top:120px;width:200px;height:200px;display:flex;flex-direction:column;align-items:center;justify-content:center;gap:10px}
.f-brand .dot{width:18px;height:18px;border-radius:50%;background:var(--white)}
.f-brand span{font-weight:600;font-size:22px;color:var(--white);text-align:center;line-height:1.2;letter-spacing:1px}
.f-head{font-weight:600;font-size:20px;color:var(--white)}
.f-list{list-style:none;color:#d9d9d9;font-size:15px;line-height:1.9}
.f-contact{list-style:none;color:#d9d9d9;font-size:15px}
.f-contact li{display:flex;gap:12px;margin-bottom:18px;align-items:flex-start}
.f-contact svg{flex:none;margin-top:3px}
.f-bottom{left:110px;top:505px;width:980px;border-top:1px solid var(--footer-line)}
.copy{left:110px;top:525px;font-size:14px;color:#cfcfcf}
.social{top:518px;display:flex;gap:10px;right:110px}
.social i{display:block;width:30px;height:30px;border:1.5px solid var(--teal);border-radius:50%}
</style>
</head>
<body>

<!-- hero background -->
<svg class="abs" style="left:0;top:0" width="1200" height="1000" viewBox="0 0 1200 1000" aria-hidden="true">
  <path d="M0 700 C250 760 420 860 700 840 C930 820 1060 740 1200 770 L1200 1000 L0 1000 Z" fill="var(--sand)"/>
  <path d="M0 790 C300 860 520 930 820 900 C1000 880 1120 850 1200 870 L1200 1000 L0 1000 Z" fill="#f7f2ea"/>
</svg>

<nav class="nav">
  <a class="active" style="left:108px">Home</a>
  <a style="left:256px">Individual Training</a>
  <a style="left:712px">Group Training</a>
  <a style="left:866px">About Me</a>
  <a class="contact" style="left:978px">CONTACT</a>
  <div class="brand"><i class="dot"></i><span>CoreBalance<br>Studio</span></div>
</nav>

<div class="abs script hero-tag">Change happens through movement and movement heals</div>
<h1 class="abs heading hero-title">Lena Hartwig Pilates Studio trainer</h1>
<a class="btn hero-btn">Request an appointment</a>
<div class="photo" role="img" aria-label="Photo of the trainer exercising on a reformer in a bright studio" style="left:560px;top:120px;width:500px;height:720px;background:linear-gradient(160deg,#e9e6e1 0%,#c9c2b8 45%,#3a3f4a 100%)"></div>

<!-- intro -->
<div class="abs script intro-label">Introduction</div>
<h2 class="abs heading intro-title">Welcome to Pilates trainer</h2>
<div class="abs intro-text">
  <p>The first prerequisite for being able to carry out our many different daily tasks with pleasure and joy is physical fitness, a consistently well-trained body and full possession of our mental powers.</p>
  <p>The comprehensive full-body training from the method's founder helps you achieve exactly this. The aim is to achieve optimal performance of the musculoskeletal system – strength, flexibility and endurance – without risk of injury. The founder originally called his method Contrology: The Art of Control. Contrology is the complete coordination of body, mind and spirit. The basic principles form the basis of all exercises with one goal: minimum effort – maximum success.</p>
</div>

<!-- offer background -->
<svg class="abs" style="left:0;top:1200px" width="1200" height="1200" viewBox="0 0 1200 1200" aria-hidden="true">
  <path d="M0 180 C300 120 600 60 900 110 C1050 135 1130 170 1200 160 L1200 1000 C900 1080 500 1120 0 1040 Z" fill="var(--sand)"/>
  <path d="M0 560 C250 620 600 700 1200 640 L1200 1000 C900 1080 500 1120 0 1040 Z" fill="#f7f2ea"/>
</svg>
<div class="abs script offer-label">What I offer</div>
<div class="abs" role="img" aria-label="Faint gold leaf ornament" style="left:40px;top:1540px;width:240px;height:180px;background:radial-gradient(ellipse at center,rgba(230,211,168,.45),rgba(230,211,168,0) 70%)"></div>

<!-- individual -->
<div class="photo" role="img" aria-label="Photo of a wooden reformer in a sunny studio" style="left:112px;top:1760px;width:240px;height:240px;background:linear-gradient(135deg,#d8b682,#a4804f)"></div>
<div class="photo" role="img" aria-label="Photo of the trainer stretching on studio equipment" style="left:372px;top:1700px;width:290px;height:380px;background:linear-gradient(160deg,#ece7df,#9f978c 60%,#4d4a48)"></div>
<h2 class="abs heading offer-title" style="left:684px;top:1670px;width:440px">Individual training</h2>
<div class="abs offer-text" style="left:684px;top:1800px;width:430px">
  <p>To get to know the Pilates method or because you don't have time to take part in group classes? Are you pursuing a specific training goal, have physical limitations or would you like to try Pilates for the first time as a beginner?</p>
  <p>Then personal training is just right for you. During individual training you are the focus and I can concentrate exclusively on you. Based on your initial physical condition, an individual training program will be developed in order to achieve your goals more quickly. The individual training takes place on the large Pilates machines (reformer, chair, tower, barrels).</p>
</div>
<a class="btn" style="left:684px;top:2160px">Download price list</a>

<!-- group -->
<h2 class="abs heading offer-title" style="left:112px;top:2350px;width:420px">Group training</h2>
<div class="abs offer-text" style="left:112px;top:2490px;width:420px">
  <p>Through consistent, correctly guided practice, you can achieve a fundamental improvement in your movement habits. The key is to provide a successful, pain-free movement experience that prevents long-term poor posture.</p>
  <p>In order to be able to offer you enough attention and assistance in carrying out the exercises, I have a limited number of participants of a maximum of 5 people. In group training, various small devices, as well as on the reformer, are used to make the lessons varied.</p>
</div>
<a class="btn" style="left:112px;top:2810px">Download price list</a>
<div class="abs" role="img" aria-label="Faint gold floral ornament" style="left:520px;top:2340px;width:680px;height:260px;background:radial-gradient(ellipse at 70% 40%,rgba(230,211,168,.4),rgba(230,211,168,0) 65%)"></div>
<div class="photo" role="img" aria-label="Photo of the trainer balancing on one leg during a class" style="left:540px;top:2420px;width:320px;height:480px;background:linear-gradient(170deg,#f0ece6,#b8aea2 55%,#3e3b3c)"></div>
<div class="photo" role="img" aria-label="Photo of a group studio with reformers" style="left:880px;top:2480px;width:240px;height:240px;background:linear-gradient(135deg,#e4c596,#b08b58)"></div>

<!-- about -->
<div class="abs" role="img" aria-label="Soft background photo of a bright Pilates studio" style="left:0;top:2980px;width:1200px;height:760px;background:linear-gradient(180deg,#e3ddd5,#cfc6ba 50%,#e6e0d8)"></div>
<section class="abs about-card">
  <div class="abs script about-label">About Me</div>
  <h2 class="abs heading about-name">Lena Hartwig</h2>
  <div class="abs about-text">
    <p>I discovered my love for Pilates several years ago and pretty quickly had the desire to teach the method and convince as many people as possible of its positive effects. I completed my training as a Pilates mat trainer very successfully at a renowned academy. In order to get to know all facets of Pilates, I trained as a studio trainer, both in the classic Pilates method and in contemporary Pilates, and I am a member of the national Pilates association and regularly take part in further training courses.</p>
    <p>I teach with fun and joy, paying great attention to the correct execution of the exercises. The focus is on quality and in order to provide you with optimal support, I generally only work in small groups or in individual and duet training.</p>
  </div>
  <div class="photo" role="img" aria-label="Portrait photo of the trainer smiling in a black top" style="left:608px;top:60px;width:340px;height:460px;background:linear-gradient(170deg,#e7e2db,#c4b59c 50%,#2f2f33)"></div>
  <div class="abs" role="img" aria-label="Gold leaf ornament" style="left:880px;top:420px;width:140px;height:200px;background:radial-gradient(ellipse at center,rgba(201,164,94,.55),rgba(201,164,94,0) 70%)"></div>
</section>

<!-- testimonials -->
<div class="abs script test-label">This is what customers say about me</div>
<h2 class="abs heading test-title">Client testimonials</h2>
<div class="quote" style="left:112px">" A technically excellent Pilates training! Each training session includes new exercise sequences with precise instructions, and different small equipment is often used. My summary: definitely try it out, highly recommended. Thanks Lena! "<b>– Sabine K.</b></div>
<div class="quote" style="left:620px">" Lena is a very good Pilates trainer. She also takes an enormous amount of time for each individual in group training sessions. It makes a lot of fun. That's why I immediately booked the 10 ticket. "<b>– Marion T.</b></div>
<div class="abs dots"><i class="on"></i><i></i><i></i></div>

<!-- footer -->
<footer class="footer">
  <svg class="abs" style="left:0;top:0" width="1200" height="580" viewBox="0 0 1200 580" aria-hidden="true">
    <path d="M0 60 C300 0 500 -10 800 30 C1000 55 1120 70 1200 40 L1200 580 L0 580 Z" fill="var(--footer)"/>
  </svg>
  <div class="abs f-brand"><i class="dot"></i><span>CoreBalance<br>Studio</span></div>
  <div class="abs" role="img" aria-label="Association membership badge" style="left:364px;top:140px;width:150px;height:180px;background:#3d5f87;border-radius:6px"></div>
  <div class="abs f-head" style="left:640px;top:130px">Quick Links</div>
  <ul class="abs f-list" style="left:640px;top:175px">
    <li>Home</li><li>Individual Training</li><li>Group Training</li><li>About Me</li><li>Contact</li>
  </ul>
  <div class="abs f-head" style="left:860px;top:130px">Contact Information</div>
  <ul class="abs f-contact" style="left:860px;top:180px;width:240px">
    <li><svg width="14" height="18" viewBox="0 0 14 18"><path d="M7 0C3.1 0 0 3.1 0 7c0 5 7 11 7 11s7-6 7-11c0-3.9-3.1-7-7-7zm0 9.5A2.5 2.5 0 1 1 7 4.5a2.5 2.5 0 0 1 0 5z" fill="var(--teal)"/></svg><span>Lindenweg 12<br>83123 Brennach</span></li>
    <li><svg width="16" height="16" viewBox="0 0 16 16"><path d="M3.6 1l2.2 3.3-1.4 1.6c.9 2 2.6 3.8 4.7 4.7l1.6-1.4L14 11.4 13 14.6C6.8 14.6 1.4 9.2 1.4 3z" fill="var(--teal)"/></svg><span>+49 170 5550182</span></li>
    <li><svg width="16" height="13" viewBox="0 0 16 13"><rect x="0.5" y="0.5" width="15" height="12" fill="none" stroke="var(--teal)"/><path d="M1 1l7 6 7-6" fill="none" stroke="var(--teal)"/></svg><span>info@movewell-brennach.de</span></li>
  </ul>
  <div class="abs f-bottom"></div>
  <div class="abs copy">© 2024, Copyright Lena Hartwig | Pilates Glossary | Privacy Policy | Imprint</div>
  <div class="abs social"><i></i><i></i><i></i></div>
</footer>

</body>
</html>
```